Peaks4U LOGO + Business Card design for a Ski Tour agency

- New start-up international tour agency focused on skiing tours
- Connected with the Alps
- Targeted at Asians
- Business/Brand name: Peaks4U

```html
<!DOCTYPE html>
<html lang="en">
<head>
<meta charset="utf-8">
<title>Peaks4U Business Card</title>
<link href="https://fonts.googleapis.com/css2?family=Roboto:wght@400;500;700;900&display=swap" rel="stylesheet">
<style>
  :root {
    --backdrop: #ebe8e3;
    --card: #ffffff;
    --ink: #1b1b1b;
    --ink-soft: #2c2c2c;
    --brand-navy: #1d5a97;
    --brand-blue: #2a9ad8;
    --wave-deep: #2c78c0;
    --wave-mid: #3f9ee0;
    --wave-light: #7cc6f0;
    --rule: #2d3b57;
    --pattern-a: #8cc9ec;
    --pattern-b: #b5dcf3;
    --frame: #9fd0ee;
  }
  * { margin: 0; padding: 0; box-sizing: border-box; }
  html, body { width: 900px; height: 1200px; overflow: hidden; }
  body {
    background: var(--backdrop);
    font-family: "Roboto", Arial, sans-serif;
    position: relative;
  }
  .card {
    position: absolute;
    left: 82px;
    width: 736px;
    height: 431px;
    background: var(--card);
    border-radius: 28px;
    overflow: hidden;
    box-shadow: 0 6px 18px rgba(0,0,0,0.18);
  }
  .card-front { top: 137px; }
  .card-back { top: 640px; }

  .brand {
    position: absolute;
    display: flex;
    align-items: center;
    gap: 12px;
    font-weight: 900;
    color: var(--brand-navy);
    letter-spacing: 0.5px;
  }
  .brand-dot {
    border-radius: 50%;
    background: var(--brand-blue);
    flex: none;
  }
  .card-front .brand { left: 48px; top: 70px; font-size: 56px; }
  .card-front .brand-dot { width: 56px; height: 56px; }

  .holder {
    position: absolute;
    right: 48px;
    top: 84px;
    text-align: right;
  }
  .holder-name { font-size: 25px; font-weight: 500; color: var(--ink); line-height: 1.2; }
  .holder-role { font-size: 19px; color: var(--brand-blue); line-height: 1.4; }

  .divider {
    position: absolute;
    left: 48px;
    right: 50px;
    top: 271px;
    height: 2px;
    background: var(--rule);
  }
  .contacts {
    position: absolute;
    left: 48px;
    top: 286px;
    list-style: none;
    font-size: 15.5px;
    color: var(--ink-soft);
  }
  .contacts li { display: flex; align-items: center; gap: 10px; height: 26px; }
  .contacts svg { width: 17px; height: 17px; fill: var(--brand-blue); }
  .address {
    position: absolute;
    right: 50px;
    top: 284px;
    text-align: right;
    font-size: 15.5px;
    font-style: normal;
    line-height: 24px;
    color: var(--ink-soft);
  }
  .wave { position: absolute; left: 0; top: 0; width: 736px; height: 431px; }

  .pattern {
    position: absolute;
    inset: 0;
    background: radial-gradient(circle at 30% 30%, var(--pattern-b), var(--pattern-a) 70%);
    opacity: 0.55;
  }
  .logo-panel {
    position: absolute;
    left: 170px;
    top: 145px;
    width: 391px;
    height: 140px;
    background: var(--card);
    border: 2px solid var(--frame);
    display: flex;
    align-items: center;
    justify-content: center;
  }
  .logo-panel .brand { position: static; font-size: 56px; }
  .logo-panel .brand-dot { width: 56px; height: 56px; }
</style>
</head>
<body>

<section class="card card-front">
  <svg class="wave" viewBox="0 0 736 431" aria-hidden="true">
    <path d="M0,368 C300,425 600,405 736,326 L736,431 L0,431 Z" fill="var(--wave-deep)"/>
    <path d="M0,382 C300,436 600,418 736,338 L736,431 L0,431 Z" fill="var(--wave-mid)"/>
    <path d="M0,396 C310,442 610,428 736,350 L736,431 L0,431 Z" fill="var(--wave-light)"/>
  </svg>

  <div class="brand"><span class="brand-dot"></span>Peaks4U</div>

  <div class="holder">
    <p class="holder-name">Marcus Whitfield</p>
    <p class="holder-role">Managing Director</p>
  </div>

  <div class="divider"></div>

  <ul class="contacts">
    <li>
      <svg viewBox="0 0 24 24"><path d="M6.6 10.8a15.1 15.1 0 0 0 6.6 6.6l2.2-2.2a1 1 0 0 1 1-.25 11.4 11.4 0 0 0 3.6.57 1 1 0 0 1 1 1V20a1 1 0 0 1-1 1A17 17 0 0 1 3 4a1 1 0 0 1 1-1h3.5a1 1 0 0 1 1 1c0 1.25.2 2.45.57 3.57a1 1 0 0 1-.25 1z"/></svg>
      555-014-2273
    </li>
    <li>
      <svg viewBox="0 0 24 24"><path d="M12 2a10 10 0 1 0 0 20 10 10 0 0 0 0-20zm6.9 6h-2.9a15.6 15.6 0 0 0-1.4-3.6A8 8 0 0 1 18.9 8zM12 4c.8 1.2 1.5 2.5 1.9 4h-3.8c.4-1.5 1.1-2.8 1.9-4zM4.3 14a8 8 0 0 1 0-4h3.4a16 16 0 0 0 0 4zm.8 2h2.9c.3 1.3.8 2.5 1.4 3.6A8 8 0 0 1 5.1 16zM8 8H5.1a8 8 0 0 1 4.3-3.6C8.8 5.5 8.4 6.7 8 8zm4 12c-.8-1.2-1.5-2.5-1.9-4h3.8c-.4 1.5-1.1 2.8-1.900 4zm2.3-6H9.7a14.7 14.7 0 0 1 0-4h4.6a14.7 14.7 0 0 1 0 4zm.3 5.6c.6-1.1 1.1-2.3 1.4-3.6h2.9a8 8 0 0 1-4.3 3.6zm1.7-5.6a16 16 0 0 0 0-4h3.4a8 8 0 0 1 0 4z"/></svg>
      info@peaks4u.com
    </li>
    <li>
      <svg viewBox="0 0 24 24"><path d="M2 5h20v14H2zm2 2v.5l8 5 8-5V7zm0 2.9V17h16V9.9l-8 5z"/></svg>
      www.peaks4u.com
    </li>
  </ul>

  <address class="address">
    1450, 220 9 Street N.W<br>
    Ridgeford, AB, T4K 1M8
  </address>
</section>

<section class="card card-back">
  <div class="pattern" role="img" aria-label="Scattered travel icon pattern in light blue: landmarks, planes, ships, palm trees, cameras and holiday items"></div>
  <div class="logo-panel">
    <div class="brand"><span class="brand-dot"></span>Peaks4U</div>
  </div>
</section>

</body>
</html>
```